Retractable Banners Designs for Tradeshows

We like the look and feel of the banners draft but want a more polished and improved version of the banners

The dimensions of each banner should be 33" x 80"

We want the banners to work on their own as they will be used in different places, but at tradeshows, they might be used side by side in a 10x10 tradeshow booth, so common design elements that work together is needed.
Updates

Low design quality

Target Market(s)

tradeshows booths

Colors
EB3D1F
EC4F4E
F09395
F8D3D4
FCEDEE

Requirements
Must have
• Elements that tie all the banners together, large scale images, not to cluttered or busy, designed to be visible and attractive from far away, our corporate colours are red, black, white and gray
Nice to have
• bright design not dark but using our corporate colours of red, gray, white and some black

```html
<!DOCTYPE html>
<html lang="en">
<head>
<meta charset="utf-8">
<title>Trade Show Banner Set</title>
<link href="https://fonts.googleapis.com/css2?family=Poppins:wght@400;500;800;900&display=swap" rel="stylesheet">
<style>
  :root {
    --brand-red: #e3141c;
    --brand-red-dark: #c80f17;
    --ink: #0b0b0c;
    --ink-soft: #2a2a2c;
    --paper: #ffffff;
    --mist: #eef0f3;
    --mist-deep: #dcdde0;
    --canvas-bg: #f4f4f4;
  }
  * { margin: 0; padding: 0; box-sizing: border-box; }
  html, body { width: 924px; height: 1200px; overflow: hidden; }
  body {
    background: var(--canvas-bg);
    font-family: "Poppins", sans-serif;
    display: flex;
    align-items: center;
    justify-content: center;
  }
  .banner-set {
    display: flex;
    gap: 16px;
  }
  .banner {
    position: relative;
    width: 210px;
    height: 509px;
    overflow: hidden;
    background: var(--paper);
    box-shadow: 4px 6px 12px rgba(0,0,0,0.22);
  }
  .banner-art {
    position: absolute;
    inset: 0;
    width: 210px;
    height: 509px;
  }
  .brand {
    position: absolute;
    top: 30px;
    left: 0;
    right: 0;
    display: flex;
    align-items: center;
    justify-content: center;
    gap: 5px;
    z-index: 2;
  }
  .brand-dot {
    width: 9px;
    height: 9px;
    border-radius: 50%;
    background: var(--brand-red);
  }
  .brand-name {
    font-size: 17px;
    font-weight: 400;
    color: var(--ink-soft);
    letter-spacing: 0.2px;
  }
  .title {
    position: absolute;
    left: 0;
    right: 0;
    text-align: center;
    text-transform: uppercase;
    line-height: 0.95;
    z-index: 2;
  }
  .title-main {
    display: block;
    font-weight: 900;
    color: var(--brand-red);
  }
  .title-sub {
    display: block;
    font-weight: 800;
  }
  .on-light .title-sub { color: var(--ink); }
  .on-dark .title-sub { color: var(--paper); }
  .divider-dots {
    position: absolute;
    top: 408px;
    left: 0;
    right: 0;
    display: flex;
    justify-content: center;
    gap: 3px;
    z-index: 2;
  }
  .divider-dots span {
    width: 7px;
    height: 7px;
    border-radius: 50%;
    border: 1.6px solid var(--brand-red);
    background: var(--paper);
  }
  .tagline {
    position: absolute;
    top: 427px;
    left: 14px;
    right: 14px;
    text-align: center;
    color: var(--paper);
    font-size: 12.5px;
    font-weight: 400;
    line-height: 16.5px;
    z-index: 2;
  }
</style>
</head>
<body>
<main class="banner-set">

  <section class="banner on-light">
    <svg class="banner-art" viewBox="0 0 210 509">
      <defs>
        <linearGradient id="sky-top" x1="0" y1="0" x2="0" y2="1">
          <stop offset="0" stop-color="#f1f3f8"/><stop offset="1" stop-color="#e2e5ec"/>
        </linearGradient>
        <linearGradient id="tower-photo" x1="0" y1="0" x2="0" y2="1">
          <stop offset="0" stop-color="#3c74c6"/><stop offset="0.6" stop-color="#4a82d1"/><stop offset="1" stop-color="#5d8fd4"/>
        </linearGradient>
      </defs>
      <rect width="210" height="509" fill="url(#sky-top)"/>
      <polygon points="0,300 210,290 210,509 0,509" fill="#e9eaec"/>
      <polygon role="img" aria-label="Photo of a cell tower with antennas against a blue sky" points="0,57 210,50 210,308 0,334" fill="url(#tower-photo)"/>
      <polygon points="0,334 210,308 210,312 0,339" fill="var(--ink)"/>
      <rect y="412" width="210" height="87" fill="var(--brand-red)"/>
      <rect y="499" width="210" height="10" fill="#e6e6e6"/>
      <polygon points="168,499 200,499 210,509 178,509" fill="var(--brand-red)"/>
      <polygon points="200,499 210,499 210,509" fill="var(--ink)"/>
    </svg>
    <div class="brand"><span class="brand-dot"></span><span class="brand-name">vantorel</span></div>
    <h2 class="title" style="top:347px">
      <span class="title-main" style="font-size:35px">Telecom</span>
      <span class="title-sub" style="font-size:17.5px">Infrastructure</span>
    </h2>
    <div class="divider-dots"><span></span><span></span><span></span></div>
    <p class="tagline">Cutting Edge Solutions for the Next Generation</p>
  </section>

  <section class="banner on-light">
    <svg class="banner-art" viewBox="0 0 210 509">
      <defs>
        <linearGradient id="rack-photo" x1="0" y1="0" x2="0" y2="1">
          <stop offset="0" stop-color="#c9ccd1"/><stop offset="0.18" stop-color="#4b5866"/><stop offset="1" stop-color="#27313c"/>
        </linearGradient>
      </defs>
      <rect width="210" height="509" fill="var(--mist)"/>
      <polygon role="img" aria-label="Photo of server racks in a data centre" points="0,30 210,30 210,282 0,312" fill="url(#rack-photo)"/>
      <rect width="210" height="58" fill="#f2f3f5" opacity="0.85"/>
      <polygon points="0,312 190,284 190,288 0,317" fill="var(--ink)"/>
      <circle cx="190" cy="285" r="8" fill="var(--ink)" stroke="var(--paper)" stroke-width="2"/>
      <rect y="412" width="210" height="87" fill="var(--brand-red)"/>
      <rect y="499" width="210" height="10" fill="var(--ink)"/>
      <polygon points="180,499 196,499 206,509 190,509" fill="var(--brand-red)"/>
      <polygon points="196,499 210,499 210,509 206,509" fill="var(--paper)"/>
    </svg>
    <div class="brand"><span class="brand-dot"></span><span class="brand-name">vantorel</span></div>
    <h2 class="title" style="top:334px">
      <span class="title-main" style="font-size:38px">ICT</span>
      <span class="title-sub" style="font-size:27px">Solutions</span>
    </h2>
    <div class="divider-dots"><span></span><span></span><span></span></div>
    <p class="tagline">Seamless Cable and Telecom Networks and Enterprise Deployments</p>
  </section>

  <section class="banner on-dark">
    <svg class="banner-art" viewBox="0 0 210 509">
      <defs>
        <linearGradient id="bench-photo" x1="0" y1="0" x2="1" y2="1">
          <stop offset="0" stop-color="#5a5c60"/><stop offset="0.5" stop-color="#3a3b3e"/><stop offset="1" stop-color="#6e6a66"/>
        </linearGradient>
      </defs>
      <rect width="210" height="509" fill="var(--mist)"/>
      <polygon role="img" aria-label="Photo of test and measurement instruments on a lab bench" points="0,70 210,62 210,308 0,288" fill="url(#bench-photo)"/>
      <polygon points="0,288 210,308 210,509 0,509" fill="var(--ink)"/>
      <polygon points="0,288 210,308 210,312 0,292" fill="var(--paper)"/>
      <rect y="412" width="210" height="87" fill="var(--brand-red)"/>
      <rect y="499" width="210" height="10" fill="#e6e6e6"/>
      <polygon points="170,499 186,499 196,509 180,509" fill="var(--brand-red)"/>
      <polygon points="186,499 210,499 210,509 196,509" fill="var(--ink)"/>
    </svg>
    <div class="brand"><span class="brand-dot"></span><span class="brand-name">vantorel</span></div>
    <h2 class="title" style="top:343px">
      <span class="title-main" style="font-size:37px">Text &amp;</span>
      <span class="title-sub" style="font-size:19px">Measurement</span>
    </h2>
    <div class="divider-dots"><span></span><span></span><span></span></div>
    <p class="tagline">Accurate and Efficient Solutions for the Wireless World</p>
  </section>

  <section class="banner on-dark">
    <svg class="banner-art" viewBox="0 0 210 509">
      <defs>
        <linearGradient id="worker-photo" x1="0" y1="0" x2="1" y2="1">
          <stop offset="0" stop-color="#a7a19d"/><stop offset="0.5" stop-color="#8a5f52"/><stop offset="1" stop-color="#c7b2a0"/>
        </linearGradient>
        <linearGradient id="logo-fade" x1="0" y1="0" x2="0" y2="1">
          <stop offset="0" stop-color="#f6f7f9" stop-opacity="0.95"/><stop offset="1" stop-color="#f6f7f9" stop-opacity="0"/>
        </linearGradient>
      </defs>
      <rect width="210" height="509" fill="var(--mist)"/>
      <polygon role="img" aria-label="Photo of a field technician in a hard hat working on tower equipment" points="0,0 210,0 210,330 0,308" fill="url(#worker-photo)"/>
      <polygon points="0,0 210,0 210,64 0,80" fill="url(#logo-fade)"/>
      <polygon points="0,308 210,330 210,509 0,509" fill="var(--ink)"/>
      <polygon points="0,306 210,330 210,337 0,312" fill="var(--paper)"/>
      <rect y="412" width="210" height="87" fill="var(--brand-red)"/>
      <rect y="499" width="210" height="10" fill="#e6e6e6"/>
      <polygon points="0,499 150,499 160,509 0,509" fill="var(--ink)"/>
    </svg>
    <div class="brand"><span class="brand-dot"></span><span class="brand-name">vantorel</span></div>
    <h2 class="title" style="top:366px">
      <span class="title-main" style="font-size:27px">Hardware</span>
    </h2>
    <div class="divider-dots"><span></span><span></span><span></span></div>
    <p class="tagline">High-Quality, Economical, Test Grade RF and Microwave Components</p>
  </section>

</main>
</body>
</html>
```